Design for iOS app - Scanner App

We are developing an iOS app that is scanning receipts and mailing them to a predefined email address. The app should work more or less like TallySnap app (a short demo of the TallySnap app is available here: https://www.vidloomer.com/watch?v=QpRtWx83LmK).

We have prototyped the app in the link below:
http://app.framewisp.com/view/a71c3d02b58e9f46c1d7e0a2b94f8c5d

NB!: Please do not follow the mockups literally, but the Velmor Touch Layout Handbook!

The technical specifications and descriptions of the app's functionalities are available in the link below:
https://sheets.pallowdocs.com/document/d/7mPqo-RZ2xLwQbTfHaVk9YeNuJsDcX_3Pgtn4Hmcz5/edit?usp=sharing

Requirements for the design:

- The design should be provided as PSD, where each page/section should be in its own PSD file OR all pages/sections should be represented as folder groups in a single PSD file.

- All graphical elements in the design should be delivered as single layers which can then be extracted from the PSD.

- All graphical elements (icons, graphical buttons, etc.) should be provided as vector objects in the PSD, so that they can be exported into different sizes without loss of quality (for responsiveness).

- The design should use either web safe fonts or Google Fonts.

Instructions for the design:

The design should have habitual user interface like ordinary iOS navigation stack, with navigation bar on the top and all other elements on the bottom. That means just to make the top bar in your app be more like iOS. Please follow the Velmor Touch Layout Handbook, not the mockups literally .
FX: the e small elements in Dimensions screen like delete icons and active checkbox. In
https://devs.quorrelfield.com/library/mobile/documentation/UserExperience/Conceptual/TouchGuide/LayoutandAppearance.html#//ref/doc/uid/TX50017283-CH21-SW1
is described that interface elements should be at least 44x44 px - it's normal practice for all mobile development (iOS, android), so you should consider this too.

Please also provide an app icon and suggest a logo for the app.

Requirements
Must have
• Please make sure that the design is flat. Like iOS app, Pagelift, Tessivo apps etc.
Nice to have
• The design could be somewhat like the design for Brindlemark Pagelift(https://apps.quorrelstore.com/bg/app/brindlemark-pagelift/id451927730?mt=8) without being too similar
Should not have
• 3D look

```html
<!DOCTYPE html>
<html lang="en">
<head>
<meta charset="utf-8">
<title>TallySnap – Scan</title>
<link rel="stylesheet" href="https://fonts.googleapis.com/css2?family=Roboto:wght@300;400;500&display=swap">
<style>
  :root {
    --bg-top: #324673;
    --bg-bottom: #4670a9;
    --sheen: rgba(255, 255, 255, 0.07);
    --text: #ffffff;
    --text-soft: rgba(255, 255, 255, 0.55);
    --ring: rgba(255, 255, 255, 0.55);
    --ring-faint: rgba(255, 255, 255, 0.12);
    --pending: #f26d6f;
    --sent: #62b1f8;
    --badge: #2d4671;
    --track: #2c4673;
    --fill: #ffffff;
  }
  * { margin: 0; padding: 0; box-sizing: border-box; }
  html, body { width: 1200px; height: 2194px; overflow: hidden; }
  body {
    font-family: "Roboto", sans-serif;
    color: var(--text);
    background: var(--bg-top);
  }
  .screen {
    position: relative;
    width: 1200px;
    height: 2194px;
    overflow: hidden;
    background: linear-gradient(170deg, var(--bg-top) 0%, var(--bg-bottom) 100%);
  }
  .sheen { position: absolute; inset: 0; }

  .status-bar {
    position: absolute; top: 0; left: 0; right: 0; height: 80px;
    display: flex; align-items: center; justify-content: space-between;
    padding: 0 38px; font-size: 36px; font-weight: 400;
  }
  .status-left, .status-right { display: flex; align-items: center; gap: 12px; width: 330px; }
  .status-right { justify-content: flex-end; }
  .status-time { font-weight: 500; }

  .nav-bar {
    position: absolute; top: 100px; left: 0; right: 0; height: 96px;
    display: flex; align-items: center; justify-content: center;
  }
  .nav-title { font-size: 50px; font-weight: 400; letter-spacing: 0.5px; }
  .nav-settings { position: absolute; right: 80px; top: 14px; width: 68px; height: 68px; }

  .scan-control { position: absolute; left: 0; top: 340px; width: 1200px; height: 930px; }
  .scan-label {
    position: absolute; left: 0; right: 0; top: 400px; text-align: center;
    font-size: 124px; font-weight: 300; letter-spacing: 2px; color: rgba(255,255,255,0.85);
  }

  .actions { position: absolute; top: 1522px; left: 150px; width: 923px; height: 112px; }
  .action-button {
    position: absolute; top: 0; width: 405px; height: 112px; border-radius: 6px;
    display: flex; align-items: center; justify-content: center;
    font-size: 46px; font-weight: 300; color: var(--text);
    box-shadow: 0 4px 0 rgba(0, 0, 0, 0.08);
  }
  .action-pending { left: 0; background: var(--pending); }
  .action-sent { right: 0; background: var(--sent); }
  .badge {
    position: absolute; left: 355px; top: -21px; width: 64px; height: 64px; border-radius: 50%;
    background: var(--badge); font-size: 34px; font-weight: 400;
    display: flex; align-items: center; justify-content: center;
  }

  .upload-status { position: absolute; left: 118px; width: 989px; top: 1926px; }
  .upload-label { text-align: center; font-size: 36px; font-weight: 300; color: var(--text-soft); }
  .progress-track { margin-top: 48px; height: 44px; background: var(--track); }
  .progress-fill { width: 39.3%; height: 100%; background: var(--fill); }
</style>
</head>
<body>
<main class="screen">
  <svg class="sheen" width="1200" height="2194" aria-hidden="true">
    <polygon points="638,0 1200,0 1200,1447" fill="var(--sheen)"/>
  </svg>

  <header class="status-bar">
    <div class="status-left">
      <svg width="100" height="20" aria-hidden="true">
        <circle cx="10" cy="10" r="9" fill="#fff"/>
        <circle cx="30" cy="10" r="9" fill="#fff"/>
        <circle cx="50" cy="10" r="9" fill="#fff"/>
        <circle cx="70" cy="10" r="8" fill="none" stroke="#fff" stroke-width="2"/>
        <circle cx="90" cy="10" r="8" fill="none" stroke="#fff" stroke-width="2"/>
      </svg>
      <span class="carrier">VELO</span>
      <svg width="38" height="30" viewBox="0 0 38 30" aria-hidden="true">
        <path d="M2 10 A25 25 0 0 1 36 10" fill="none" stroke="#fff" stroke-width="4"/>
        <path d="M8 16 A16 16 0 0 1 30 16" fill="none" stroke="#fff" stroke-width="4"/>
        <path d="M19 28 L13 21 A9 9 0 0 1 25 21 Z" fill="#fff"/>
      </svg>
    </div>
    <span class="status-time">4:21 PM</span>
    <div class="status-right">
      <svg width="20" height="36" viewBox="0 0 20 36" aria-hidden="true">
        <path d="M3 10 L17 24 L10 31 L10 5 L17 12 L3 26" fill="none" stroke="rgba(255,255,255,0.7)" stroke-width="2.5"/>
      </svg>
      <span>100%</span>
      <svg width="76" height="34" viewBox="0 0 76 34" aria-hidden="true">
        <rect x="1.5" y="1.5" width="66" height="31" rx="6" fill="none" stroke="#fff" stroke-width="3"/>
        <rect x="6" y="6" width="57" height="22" rx="3" fill="#fff"/>
        <rect x="70" y="11" width="5" height="12" rx="2" fill="#fff"/>
      </svg>
    </div>
  </header>

  <nav class="nav-bar">
    <h1 class="nav-title">TallySnap</h1>
    <svg class="nav-settings" viewBox="0 0 68 68" aria-label="Settings" role="img">
      <g fill="none" stroke="#fff" stroke-width="3" stroke-linejoin="round">
        <path d="M29 5 h10 l2 8 l6 3 l7-4 l7 7 l-4 7 l3 6 l8 2 v10 l-8 2 l-3 6 l4 7 l-7 7 l-7-4 l-6 3 l-2 8 h-10 l-2-8 l-6-3 l-7 4 l-7-7 l4-7 l-3-6 l-8-2 v-10 l8-2 l3-6 l-4-7 l7-7 l7 4 l6-3 z"/>
        <circle cx="34" cy="34" r="9"/>
      </g>
    </svg>
  </nav>

  <section class="scan-control">
    <svg width="1200" height="930" aria-hidden="true">
      <circle cx="600" cy="465" r="435" fill="none" stroke="var(--ring-faint)" stroke-width="2"/>
      <circle cx="600" cy="465" r="310" fill="none" stroke="var(--ring)" stroke-width="3"/>
      <path d="M600 155 A310 310 0 0 1 910 465" fill="none" stroke="#fff" stroke-width="9"/>
    </svg>
    <div class="scan-label">SCAN</div>
  </section>

  <section class="actions">
    <div class="action-button action-pending">Pending</div>
    <div class="badge">3</div>
    <div class="action-button action-sent">Sent</div>
  </section>

  <section class="upload-status">
    <p class="upload-label">Sending an Email :</p>
    <div class="progress-track"><div class="progress-fill"></div></div>
  </section>
</main>
</body>
</html>
```